Business Reporting Graph Illustration

I'm looking for a graphic design to created an illustration of a line chart I have two sample charts that I'd like elements of each combined together to create the project. Below is a link to learn more about this project. This should be designed using any product of the Adobe Suite.
Color Scheme is included within the below link. This will require 2 - 3 rounds of design before final completion.

https://www.plonvadesk.com/file/QWT8HbxuLeMRa302KD5Vpt/Graphic-Design-Project

```html
<!DOCTYPE html>
<html lang="en">
<head>
<meta charset="utf-8">
<title>Attribution Window Line Chart</title>
<link rel="stylesheet" href="https://fonts.googleapis.com/css2?family=Montserrat:wght@400;500;700&display=swap">
<style>
  :root {
    --ink: #0f1c3f;
    --bar-blue: #5a81b2;
    --response-line: #f9b11c;
    --marker-fill: #ffffff;
    --page: #ffffff;
  }
  html, body {
    margin: 0;
    padding: 0;
    width: 1200px;
    height: 560px;
    overflow: hidden;
    background: var(--page);
  }
  .chart {
    display: block;
    width: 1200px;
    height: 560px;
    font-family: "Montserrat", sans-serif;
  }
  .axis-line, .axis-tick { stroke: var(--ink); stroke-width: 1.6; }
  .axis-title { fill: var(--ink); font-size: 21px; font-weight: 500; letter-spacing: 0.3px; }
  .axis-label { fill: var(--ink); font-size: 19px; font-weight: 400; text-anchor: middle; }
  .ad-window { fill: var(--bar-blue); }
  .ad-label { fill: var(--ink); font-size: 13.5px; font-weight: 700; text-anchor: middle; }
  .window-label { fill: var(--ink); font-size: 11.5px; font-weight: 400; text-anchor: middle; }
  .response-curve { fill: none; stroke: var(--response-line); stroke-width: 2.8; stroke-linecap: round; stroke-linejoin: round; }
  .ad-marker { fill: var(--marker-fill); }
  .direct-dot { fill: var(--bar-blue); }
  .direct-stem { stroke: var(--bar-blue); stroke-width: 1.6; stroke-dasharray: 5 3.5; }
  .direct-label { fill: var(--bar-blue); font-size: 9.6px; font-weight: 400; }
</style>
</head>
<body>
<svg class="chart" viewBox="0 0 1200 560" xmlns="http://www.w3.org/2000/svg">
  <!-- ad attribution windows -->
  <g class="ad-windows">
    <path class="ad-window" d="M450.7 430.5 V224.3 A28.65 28.65 0 0 1 508 224.3 V430.5 Z"/>
    <path class="ad-window" d="M737.7 430.5 V351.4 A28.7 28.7 0 0 1 795.1 351.4 V430.5 Z"/>
    <path class="ad-window" d="M910 430.5 V405.3 A28.7 28.7 0 0 1 967.4 405.3 V430.5 Z"/>
  </g>

  <text class="window-label" transform="translate(483 317) rotate(-90)">Attribution window</text>

  <!-- time axis -->
  <g class="axis">
    <line class="axis-line" x1="141" y1="430.5" x2="1175" y2="430.5"/>
    <g class="axis-ticks">
      <line class="axis-tick" x1="278.6" y1="430.5" x2="278.6" y2="440"/>
      <line class="axis-tick" x1="335.8" y1="430.5" x2="335.8" y2="440"/>
      <line class="axis-tick" x1="393" y1="430.5" x2="393" y2="440"/>
      <line class="axis-tick" x1="450.7" y1="430.5" x2="450.7" y2="440"/>
      <line class="axis-tick" x1="507.9" y1="430.5" x2="507.9" y2="440"/>
      <line class="axis-tick" x1="565.6" y1="430.5" x2="565.6" y2="440"/>
      <line class="axis-tick" x1="622.8" y1="430.5" x2="622.8" y2="440"/>
      <line class="axis-tick" x1="680.5" y1="430.5" x2="680.5" y2="440"/>
      <line class="axis-tick" x1="737.7" y1="430.5" x2="737.7" y2="440"/>
      <line class="axis-tick" x1="795.4" y1="430.5" x2="795.4" y2="440"/>
      <line class="axis-tick" x1="852.6" y1="430.5" x2="852.6" y2="440"/>
      <line class="axis-tick" x1="909.9" y1="430.5" x2="909.9" y2="440"/>
      <line class="axis-tick" x1="967.5" y1="430.5" x2="967.5" y2="440"/>
      <line class="axis-tick" x1="1024.8" y1="430.5" x2="1024.8" y2="440"/>
      <line class="axis-tick" x1="1082" y1="430.5" x2="1082" y2="440"/>
    </g>
    <text class="axis-title" x="48" y="438">MINUTES</text>
    <g class="axis-labels">
      <text class="axis-label" x="252" y="457">1</text>
      <text class="axis-label" x="312" y="457">2</text>
      <text class="axis-label" x="369" y="457">3</text>
      <text class="axis-label" x="428" y="457">4</text>
      <text class="axis-label" x="484" y="457">5</text>
      <text class="axis-label" x="542" y="457">6</text>
      <text class="axis-label" x="599" y="457">7</text>
      <text class="axis-label" x="657" y="457">8</text>
      <text class="axis-label" x="714" y="457">9</text>
      <text class="axis-label" x="775" y="457">10</text>
      <text class="axis-label" x="830" y="457">11</text>
      <text class="axis-label" x="889" y="457">12</text>
      <text class="axis-label" x="946" y="457">13</text>
      <text class="axis-label" x="1004" y="457">14</text>
      <text class="axis-label" x="1061" y="457">15</text>
    </g>
  </g>

  <!-- direct response marker -->
  <g class="direct-response">
    <line class="direct-stem" x1="150.5" y1="282" x2="150.5" y2="406"/>
    <circle class="direct-dot" cx="150.5" cy="276.7" r="5.2"/>
    <text class="direct-label" x="160.5" y="280.5">Direct</text>
    <text class="direct-label" x="160.5" y="291.7">Response</text>
  </g>

  <!-- response over time -->
  <path class="response-curve" d="M147 411 C162 416 170 422 178 430 S188 440 198 438 S214 432 225 425 S240 414 253 414 S275 400 300 371 S312 354 324 349 S360 332 375 314 S392 280 400 264 S415 225 450 216 S465 217 469 219 S483 228 490 235 S520 265 539 279 S575 293 596 303 S615 318 624 326 S645 348 671 354 S710 340 722 333 S738 324 748 330 S760 348 775 360 S795 364 812 357 S830 345 844 341 S870 332 882 347 S905 382 915 393 S935 413 960 416 S990 408 1008 404 S1020 400 1032 402 S1060 406 1079 412 S1130 426 1168 419"/>

  <!-- ad moments -->
  <g class="ad-markers">
    <circle class="ad-marker" cx="480.3" cy="224.7" r="13.2"/>
    <circle class="ad-marker" cx="766.8" cy="351.8" r="13.2"/>
    <circle class="ad-marker" cx="939" cy="405.7" r="13.2"/>
  </g>

  <g class="ad-labels">
    <text class="ad-label" x="480" y="190">TV Ad</text>
    <text class="ad-label" x="767" y="317">TV Ad</text>
    <text class="ad-label" x="939" y="372">Radio Ad</text>
  </g>
</svg>
</body>
</html>
```